Kova upkeep RT Sun Systems

Solar power system install
Services and maintenance
wiring, Rewinding and Renovation
Switch Board Upgrade
Power and lighting point
t doesn’t matter how much you spend on quality parts, your solar system will let you down if your design and installation are sub-par. Have your solar system tailored and installed by our Master Electrician and Bright Power Guild Accredited team.

Target Market(s)

sales and installed

Industry/Entity Type

Solar install and retailer

Contact Information for Business Card

Name , Email, Phone Number ,Business address,

Font styles to use
Serif

Colors
0054AA
0677BA
7BADD7
CADEEF
E8F1F8

Requirements
Must have
• clear and bright
Nice to have
• new design
Should not have
• unclear pictures

```html
<!DOCTYPE html>
<html lang="en">
<head>
<meta charset="utf-8">
<title>Business Card</title>
<link rel="stylesheet" href="https://fonts.googleapis.com/css2?family=Barlow:ital,wght@0,400;0,500;0,600;0,700;1,400&display=swap">
<style>
  :root {
    --navy: #25215f;
    --sky: #9dbde3;
    --paper: #f7f7f8;
    --ink: #151515;
    --stage: #ecedf0;
    --panel-dark: #1f2a6b;
    --panel-light: #4a63a8;
  }
  * { box-sizing: border-box; margin: 0; padding: 0; }
  html, body {
    width: 900px; height: 1200px; overflow: hidden;
    background: var(--stage);
    font-family: "Barlow", sans-serif;
  }
  .canvas { position: relative; width: 900px; height: 1200px; }

  .card {
    position: absolute; width: 774px; height: 447px;
    border-radius: 22px; overflow: hidden;
    box-shadow: 0 4px 14px rgba(0,0,0,.12);
  }
  .card-front { left: 72px; top: 136px; background: var(--paper); }
  .card-back  { left: 74px; top: 625px; background: var(--sky); }

  .card-shapes { position: absolute; inset: 0; }

  .holder-name {
    position: absolute; left: 0; width: 412px; top: 75px;
    text-align: center; font-size: 34px; font-weight: 600;
    letter-spacing: 1.6px; color: var(--ink);
  }
  .holder-role {
    position: absolute; left: 0; width: 412px; top: 116px;
    text-align: center; font-size: 26px; letter-spacing: 2px; color: var(--ink);
  }
  .contact-icons { position: absolute; left: 36px; top: 203px; }
  .contact-list {
    position: absolute; left: 0; width: 408px; top: 283px;
    list-style: none; text-align: center;
    font-size: 22.5px; line-height: 31px; color: var(--ink);
  }
  .logo-mark {
    position: absolute; right: 50px; top: 53px;
    text-align: right; font-size: 80px; font-weight: 700;
    line-height: 70px; color: #fff;
  }

  .service-list { list-style: none; }
  .service {
    position: absolute; font-size: 28px; font-weight: 700;
    letter-spacing: 0.4px; color: var(--navy); white-space: nowrap;
  }
  .service::before {
    content: ""; position: absolute; left: -20px; top: 14px;
    width: 12px; height: 12px; border-radius: 50%; background: var(--navy);
  }
  .pitch { font-style: italic; font-size: 19.5px; color: var(--navy); }
  .pitch span { position: absolute; white-space: nowrap; }
</style>
</head>
<body>
<main class="canvas">

  <section class="card card-front" aria-label="Business card front">
    <svg class="card-shapes" width="774" height="447" viewBox="0 0 774 447" aria-hidden="true">
      <polygon points="323,0 774,0 774,447 558,447" fill="var(--navy)"/>
      <polygon points="468,272 558,447 323,447" fill="var(--sky)"/>
    </svg>

    <h1 class="holder-name">Johnathan Doe</h1>
    <p class="holder-role">Owner</p>

    <svg class="contact-icons" width="340" height="40" viewBox="0 0 340 40" aria-hidden="true">
      <path d="M0 20 L95 19 L95 21 Z" fill="var(--navy)"/>
      <path d="M235 19 L330 20 L235 21 Z" fill="var(--navy)"/>
      <circle cx="121" cy="20" r="17" fill="var(--navy)"/>
      <path d="M114 12 q-2 2 0 6 q4 8 11 11 q3 1 5 -1 l-3 -4 q-2 1 -3 0 q-4 -3 -6 -6 q-1 -2 1 -3 z" fill="#fff"/>
      <circle cx="165" cy="20" r="17" fill="var(--navy)"/>
      <rect x="156" y="14" width="18" height="12" rx="1.5" fill="#fff"/>
      <path d="M156 15 L165 22 L174 15" stroke="var(--navy)" stroke-width="1.6" fill="none"/>
      <circle cx="209" cy="20" r="17" fill="var(--navy)"/>
      <g stroke="#fff" stroke-width="1.5" fill="none">
        <circle cx="209" cy="20" r="9"/>
        <ellipse cx="209" cy="20" rx="4" ry="9"/>
        <line x1="200" y1="20" x2="218" y2="20"/>
        <line x1="202" y1="15" x2="216" y2="15"/>
        <line x1="202" y1="25" x2="216" y2="25"/>
      </g>
    </svg>

    <ul class="contact-list">
      <li>123 456 7890</li>
      <li>email@domainnamehere.com</li>
      <li>www.websitegoeshere.com</li>
    </ul>

    <div class="logo-mark">LOGO<br>HERE</div>
  </section>

  <section class="card card-back" aria-label="Business card back">
    <svg class="card-shapes" width="773" height="447" viewBox="0 0 773 447">
      <defs>
        <linearGradient id="panelTone" x1="0" y1="0" x2="1" y2="1">
          <stop offset="0" stop-color="var(--panel-light)"/>
          <stop offset="0.6" stop-color="var(--panel-dark)"/>
          <stop offset="1" stop-color="var(--panel-light)"/>
        </linearGradient>
      </defs>
      <polygon role="img" aria-label="Photo of a solar panel corner with its metal frame"
               points="0,0 14,0 470,447 0,447" fill="url(#panelTone)"/>
    </svg>

    <ul class="service-list">
      <li class="service" style="left:114px;top:41px">Solar Power System Install</li>
      <li class="service" style="left:156px;top:83px">Services And Maintenance</li>
      <li class="service" style="left:200px;top:124px">Wiring, Rewinding And Renovation</li>
      <li class="service" style="left:254px;top:165px">Switch Board Upgrade</li>
      <li class="service" style="left:302px;top:207px">Power And Lighting Point</li>
    </ul>

    <p class="pitch">
      <span style="left:324px;top:274px">It doesn’t matter how much you spend on quality</span>
      <span style="left:349px;top:296px">parts, your solar system will let you down if your</span>
      <span style="left:372px;top:318px">design and installation are sub-par. Have your</span>
      <span style="left:394px;top:341px">solar system tailored and installed by our</span>
      <span style="left:419px;top:364px">Master Electrician and Bright Power Guild</span>
      <span style="left:442px;top:386px">Accredited team.</span>
    </p>
  </section>

</main>
</body>
</html>
```